New Website Design (Uncoded) Competition for Lorvex Trade Link

Please submit design concepts for a Joomla 3.0 Website for LORVEX TRADE LINK company. Our client prefers a modem style design, responsive to all mobile devices,
The website demo content needs to be clear and detailed.

Menu sample:
Home/About Us/Service/Strength/Partner/News/Contact US/Blog

Requirements:
1. Only need to submit the PSD for the design, coding work is not included.
2. Please submit both Homepage and Inner page to demonstrate the concept.
3. The Homepage needs to include: LOGO/MENU/Banner/Language Switcher/Company Introduction/Welcome module/Advertising Module/Footer Menu/Footer/Copyright/Social Links
4. Use Asian business women for demo pictures/Could try city pictures for background.
5. Prefer SINGLE SCREEN design rather than scrollable multiple screen designs.
6. Avoid any chain symbol since the company is more about financial business.
7. Avoid any direct connotations related with money or cash.
Updates

Hi Designers, I have clearly state the requirements that avoid using neg connontation pictures like cash/ property, though still receive concepts like that. Please check the brief clearly and mark at Update with "cheers" Kel from VT

Target Market(s)

Dongrui Lorvex Trade link Company provide cross-border Supply chain Financial service by integrating Dongrui Trade Link resource.
The Company mission is become the most respectful, professional and valuable Chinese Supply Chain Financial Company, pioneer the supply chain industry.

Industry/Entity Type

Financial

Font styles to use
Sans Serif

Colors
33b7a4

Requirements
Must have
• 1. Necessary Web element, including Logo/navigation/ Banner/ Footer
2. Asia business Women pictures.
Should not have
• 6. Avoid any chain symbol since the company is more about financial business.

```html
<!DOCTYPE html>
<html lang="en">
<head>
<meta charset="utf-8">
<title>About Us – Lorvex Trade Link</title>
<link rel="stylesheet" href="https://fonts.googleapis.com/css2?family=Roboto:wght@300;400;500;700&family=Roboto+Condensed:wght@700&display=swap">
<style>
  :root {
    --ink: #111111;
    --text: #1c1c1c;
    --muted: #7a7a7a;
    --accent: #2a8fd0;
    --overlay: #1f78bd;
    --header-bg: #f6f6f6;
    --rule: #d6d6d6;
    --photo-man: #5a4c52;
    --photo-man-dark: #3a3038;
    --photo-woman: #2a2522;
    --photo-woman-light: #b5a292;
  }
  * { margin: 0; padding: 0; box-sizing: border-box; }
  html, body { width: 1200px; height: 754px; overflow: hidden; background: #ffffff; }
  body { position: relative; font-family: "Roboto", sans-serif; color: var(--text); }

  .site-header { position: absolute; top: 0; left: 0; width: 1200px; height: 67px; background: var(--header-bg); }
  .brand { position: absolute; left: 160px; top: 20px; display: flex; align-items: center; gap: 9px; }
  .brand-dot { width: 22px; height: 22px; border-radius: 50%; background: var(--accent); }
  .brand-name { font-family: "Roboto", sans-serif; font-weight: 700; font-size: 19px; color: #555a60; letter-spacing: 0.2px; }

  .main-nav { position: absolute; left: 380px; top: 24px; display: flex; gap: 18px; }
  .main-nav a { font-family: "Roboto Condensed", sans-serif; font-weight: 700; font-size: 15px; color: var(--ink); text-decoration: none; letter-spacing: 0.2px; }
  .main-nav a.is-active { color: var(--accent); }

  .lang-switch { position: absolute; right: 150px; top: 26px; font-size: 12px; font-weight: 300; color: var(--muted); display: flex; align-items: center; gap: 4px; }
  .lang-switch svg { width: 9px; height: 6px; }

  .history { position: absolute; top: 124px; width: 414px; }
  .history--company { left: 159px; }
  .history--success { left: 629px; }
  .history h2 { font-family: "Roboto Condensed", sans-serif; font-weight: 700; font-size: 21px; color: var(--ink); letter-spacing: 0.1px; margin-bottom: 10px; }
  .history p { font-size: 13.6px; line-height: 19.7px; color: var(--text); }

  .team-heading { position: absolute; top: 369px; left: 152px; width: 881px; display: flex; align-items: center; gap: 16px; }
  .team-heading::before, .team-heading::after { content: ""; flex: 1; height: 1px; background: var(--ink); }
  .team-heading h2 { font-family: "Roboto Condensed", sans-serif; font-weight: 700; font-size: 20px; color: var(--ink); }

  .team-member { position: absolute; top: 439px; width: 182px; height: 182px; }
  .team-member svg { display: block; }
  .member-1 { left: 159px; }
  .member-2 { left: 394px; }
  .member-3 { left: 627px; }
  .member-4 { left: 862px; }
  .details-label { font-family: "Roboto", sans-serif; font-size: 16.5px; font-weight: 400; fill: #ffffff; letter-spacing: 0.4px; }

  .site-footer { position: absolute; top: 695px; left: 0; width: 1200px; height: 59px; border-top: 1px solid var(--rule); }
  .copyright { position: absolute; left: 150px; top: 29px; font-size: 12px; font-weight: 300; color: #6a6a6a; }
  .copyright a { color: #6a6a6a; text-decoration: underline; }
  .copyright .sep { margin: 0 4px; }
  .social-links { position: absolute; right: 150px; top: 20px; display: flex; gap: 16px; }
  .social-links span { width: 21px; height: 21px; border: 1.5px solid #7c7c7c; border-radius: 50%; }
</style>
</head>
<body>
  <header class="site-header">
    <div class="brand">
      <span class="brand-dot"></span>
      <span class="brand-name">LORVEX TRADE LINK</span>
    </div>
    <nav class="main-nav">
      <a href="#" class="is-active">ABOUT US</a>
      <a href="#">SERVICE</a>
      <a href="#">STRENGTH</a>
      <a href="#">PARTNER</a>
      <a href="#">NEWS</a>
      <a href="#">CONTACT US</a>
      <a href="#">BLOG</a>
    </nav>
    <div class="lang-switch">Choose Language
      <svg viewBox="0 0 9 6"><path d="M0.5 0.8 L4.5 4.8 L8.5 0.8" fill="none" stroke="#7a7a7a" stroke-width="1"/></svg>
    </div>
  </header>

  <section class="history history--company">
    <h2>THE HISTORY OF THE COMPANY</h2>
    <p>Pellentesque mauris mi, laoreet a nisi bibendum, bibendum mollis lacus. Nulla sodales risus non lobortis lobortis. In sit amet placerat lorem. Ut eu augue at nisi dapibus sollicitudin sed et neque. Vetibulum sollicitudin orci nunc, ut gravida quam tincidunt eu. Morbi augue dui, malesuada vitae turpis at, pharetra iaculis libero. Nullam fermentum consequat congue. Suspenisse pharetra egetas sagittis. Maecenas nisi lacus, molestie quis venenatis vel, iaculis venenatis orci. In venenatis pulvinar lobortis.</p>
  </section>

  <section class="history history--success">
    <h2>THE HISTORY OF SUCCESS</h2>
    <p>Curabitur ultricies, tortor id tincidunt cursus, nunc enim iaculis libero, ac accumsan enim enim at diam. Ut elementum molestie nisl sed consequat. Maecenas eget purus dolor. Cras non felis egestas, pretium ante a, metus. Praesent at velit ultricies, intedum lacus vitae, ullamcorper mauris. Nam nunc erat, venenatis nec leo at, bibendum dignissim magna. Cras vel auctor sapien. Vivamus sit amet purus rutrum, rutrum libero id.</p>
  </section>

  <div class="team-heading"><h2>OUR TEAM</h2></div>

  <div class="team-member member-1">
    <svg width="182" height="182" viewBox="0 0 182 182" role="img" aria-label="Portrait photo of a team member, a man in a suit">
      <defs><radialGradient id="manTone" cx="50%" cy="45%" r="60%"><stop offset="0" stop-color="#8a6e66"/><stop offset="1" stop-color="#3a3038"/></radialGradient></defs>
      <circle cx="91" cy="91" r="91" fill="url(#manTone)"/>
    </svg>
  </div>

  <div class="team-member member-2">
    <svg width="182" height="182" viewBox="0 0 182 182" role="img" aria-label="Portrait photo of a team member, a businesswoman, with a click for details overlay">
      <defs><clipPath id="circleClip"><circle cx="91" cy="91" r="91"/></clipPath></defs>
      <circle cx="91" cy="91" r="91" fill="var(--overlay)"/>
      <g clip-path="url(#circleClip)" stroke="#ffffff" stroke-opacity="0.45" stroke-width="1">
        <line x1="0" y1="109" x2="90" y2="109"/>
        <line x1="0" y1="121" x2="90" y2="121"/>
        <line x1="0" y1="133" x2="90" y2="133"/>
        <line x1="0" y1="145" x2="90" y2="145"/>
        <line x1="0" y1="157" x2="90" y2="157"/>
        <line x1="0" y1="169" x2="90" y2="169"/>
      </g>
      <text class="details-label" x="91" y="100" text-anchor="middle">CLICK FOR DETAILS</text>
    </svg>
  </div>

  <div class="team-member member-3">
    <svg width="182" height="182" viewBox="0 0 182 182" role="img" aria-label="Portrait photo of a team member, a man in a suit">
      <circle cx="91" cy="91" r="91" fill="url(#manTone)"/>
    </svg>
  </div>

  <div class="team-member member-4">
    <svg width="182" height="182" viewBox="0 0 182 182" role="img" aria-label="Portrait photo of a team member, a smiling businesswoman">
      <defs><radialGradient id="womanTone" cx="50%" cy="50%" r="60%"><stop offset="0" stop-color="#c9a48e"/><stop offset="0.55" stop-color="#6b4f43"/><stop offset="1" stop-color="#1f1a18"/></radialGradient></defs>
      <circle cx="91" cy="91" r="91" fill="url(#womanTone)"/>
    </svg>
  </div>

  <footer class="site-footer">
    <p class="copyright">©2014 Lorvex Trade Link. All Rights Reserved. <a href="#">Privacy Policy</a><span class="sep">|</span><a href="#">News</a><span class="sep">|</span><a href="#">Contact Us</a></p>
    <div class="social-links">
      <span role="img" aria-label="Social link"></span>
      <span role="img" aria-label="Social link"></span>
      <span role="img" aria-label="Social link"></span>
    </div>
  </footer>
</body>
</html>
```